professional business card design

Business card design. Photos have been uploaded and i am open to the designer choosing which photos to use. Would like the card to be mostyly in a grey scale design with black, whites, silver & grey colours. I have added copy of our flyer as would like on the back side of card our services to be listed. Do not use any bright colurs such as blue red green or yellow. i need to be able to edit the phone number and naem in the final card design submitted.

Target Market(s)

Clients

Industry/Entity Type

earhmovibng and transport

Contact Information for Business Card

Director Name, address, email, phone number and services

Colors

Designer to choose only greyscale colors for use in the design.

Requirements
Should not have
• no yellow, red, blue or green

```html
<!DOCTYPE html>
<html lang="en">
<head>
<meta charset="utf-8">
<title>KTR Pty Ltd – Business Card</title>
<link href="https://fonts.googleapis.com/css2?family=Lato:wght@400;700;900&display=swap" rel="stylesheet">
<style>
  :root {
    --page: #3a3a3a;
    --card: #0b0b0b;
    --card-mid: #1c1c1c;
    --silver-light: #f2f2f2;
    --silver: #bdbdbd;
    --silver-dark: #6e6e6e;
    --text-white: #ffffff;
    --text-grey: #c9c9c9;
    --text-muted: #9a9a9a;
  }
  * { box-sizing: border-box; margin: 0; padding: 0; }
  html, body { width: 1200px; height: 962px; overflow: hidden; }
  body {
    background: var(--page);
    font-family: "Lato", sans-serif;
    position: relative;
  }
  .card {
    position: absolute;
    left: 280px;
    width: 640px;
    height: 366px;
    border-radius: 22px;
    background: var(--card);
    overflow: hidden;
    box-shadow: 0 14px 30px rgba(0,0,0,.45);
  }
  .card--services { top: 80px; background: linear-gradient(135deg, #1a1a1a, #0d0d0d 60%, #161616); }
  .card--contact { top: 506px; }

  /* services side */
  .truck-photo {
    position: absolute; left: 0; top: 0; width: 330px; height: 366px;
    background: linear-gradient(160deg, #d9dde0 0%, #9ea3a7 45%, #55585a 80%, #1a1a1a 100%);
  }
  .services-band { position: absolute; right: 0; top: 60px; width: 300px; height: 70px; }
  .services-title {
    position: absolute; right: 28px; top: 80px;
    font-weight: 900; font-size: 24px; color: #111; letter-spacing: .5px;
  }
  .services-list {
    position: absolute; right: 24px; top: 140px;
    list-style: none; text-align: right;
  }
  .services-list li {
    font-size: 15px; line-height: 17.6px; color: var(--text-white);
    display: flex; justify-content: flex-end; align-items: center; gap: 6px;
  }
  .tick { width: 12px; height: 12px; flex: none; }

  /* contact side */
  .mesh-panel {
    position: absolute; left: 230px; top: 30px; width: 410px; height: 250px;
    background: radial-gradient(ellipse at 70% 40%, #4a4a4a 0%, #2a2a2a 45%, rgba(11,11,11,0) 80%);
  }
  .silver-band { position: absolute; left: 0; top: 0; width: 640px; height: 366px; }
  .brand {
    position: absolute; left: 380px; top: 88px; width: 230px; text-align: center;
    color: var(--silver); font-weight: 900; line-height: 1;
  }
  .brand__name { font-size: 92px; letter-spacing: 4px; display: block; }
  .brand__suffix { font-size: 24px; display: block; margin-top: 4px; }
  .person { position: absolute; left: 40px; top: 150px; }
  .person__name { font-size: 30px; font-weight: 900; color: var(--text-grey); letter-spacing: .5px; }
  .person__title { font-size: 20px; color: var(--text-grey); margin-top: 2px; }
  .person__rule { width: 130px; height: 2px; background: var(--text-white); margin-top: 10px; }
  .contact-line {
    display: flex; align-items: center; gap: 12px; margin-top: 10px;
    color: var(--text-white); font-size: 20px;
  }
  .contact-line--email { font-size: 18px; color: var(--text-grey); margin-top: 6px; }
  .contact-line svg { width: 16px; height: 16px; flex: none; }
  .address {
    position: absolute; right: 40px; top: 280px; text-align: right;
    font-size: 18px; line-height: 26px; color: var(--text-grey);
  }
</style>
</head>
<body>

<section class="card card--services">
  <div class="truck-photo" role="img" aria-label="Photo of a white prime mover truck with an oversize sign on the bull bar"></div>
  <svg class="services-band" viewBox="0 0 300 70" aria-hidden="true">
    <defs>
      <linearGradient id="bandSilver" x1="0" y1="0" x2="1" y2="0">
        <stop offset="0" stop-color="#8a8a8a"/>
        <stop offset="0.35" stop-color="#f4f4f4"/>
        <stop offset="1" stop-color="#a9a9a9"/>
      </linearGradient>
    </defs>
    <polygon points="0,0 300,0 300,70 40,70" fill="url(#bandSilver)"/>
  </svg>
  <h2 class="services-title">OUR SERVICES</h2>
  <ul class="services-list">
    <li>Over Size Loads / Hot Shot Loads <svg class="tick" viewBox="0 0 12 12"><circle cx="6" cy="6" r="6" fill="#fff"/><path d="M3.2 6.2l1.9 1.9 3.7-3.9" stroke="#111" stroke-width="1.6" fill="none"/></svg></li>
    <li>Heavy Vehicle Recovery Services <svg class="tick" viewBox="0 0 12 12"><circle cx="6" cy="6" r="6" fill="#fff"/><path d="M3.2 6.2l1.9 1.9 3.7-3.9" stroke="#111" stroke-width="1.6" fill="none"/></svg></li>
    <li>Poatable Water Deliveries <svg class="tick" viewBox="0 0 12 12"><circle cx="6" cy="6" r="6" fill="#fff"/><path d="M3.2 6.2l1.9 1.9 3.7-3.9" stroke="#111" stroke-width="1.6" fill="none"/></svg></li>
    <li>Road Building / Maintenance <svg class="tick" viewBox="0 0 12 12"><circle cx="6" cy="6" r="6" fill="#fff"/><path d="M3.2 6.2l1.9 1.9 3.7-3.9" stroke="#111" stroke-width="1.6" fill="none"/></svg></li>
    <li>Earthworks <svg class="tick" viewBox="0 0 12 12"><circle cx="6" cy="6" r="6" fill="#fff"/><path d="M3.2 6.2l1.9 1.9 3.7-3.9" stroke="#111" stroke-width="1.6" fill="none"/></svg></li>
    <li>Sand &amp; Metal Supply &amp; Cartage <svg class="tick" viewBox="0 0 12 12"><circle cx="6" cy="6" r="6" fill="#fff"/><path d="M3.2 6.2l1.9 1.9 3.7-3.9" stroke="#111" stroke-width="1.6" fill="none"/></svg></li>
    <li>Road Train Tippers <svg class="tick" viewBox="0 0 12 12"><circle cx="6" cy="6" r="6" fill="#fff"/><path d="M3.2 6.2l1.9 1.9 3.7-3.9" stroke="#111" stroke-width="1.6" fill="none"/></svg></li>
    <li>Road Train Tankers <svg class="tick" viewBox="0 0 12 12"><circle cx="6" cy="6" r="6" fill="#fff"/><path d="M3.2 6.2l1.9 1.9 3.7-3.9" stroke="#111" stroke-width="1.6" fill="none"/></svg></li>
    <li>Road Train Flat Tops <svg class="tick" viewBox="0 0 12 12"><circle cx="6" cy="6" r="6" fill="#fff"/><path d="M3.2 6.2l1.9 1.9 3.7-3.9" stroke="#111" stroke-width="1.6" fill="none"/></svg></li>
    <li>Drop Dect Trailers <svg class="tick" viewBox="0 0 12 12"><circle cx="6" cy="6" r="6" fill="#fff"/><path d="M3.2 6.2l1.9 1.9 3.7-3.9" stroke="#111" stroke-width="1.6" fill="none"/></svg></li>
    <li>Mine Site Accredited <svg class="tick" viewBox="0 0 12 12"><circle cx="6" cy="6" r="6" fill="#fff"/><path d="M3.2 6.2l1.9 1.9 3.7-3.9" stroke="#111" stroke-width="1.6" fill="none"/></svg></li>
    <li>Equipment &amp; Operators <svg class="tick" viewBox="0 0 12 12"><circle cx="6" cy="6" r="6" fill="#fff"/><path d="M3.2 6.2l1.9 1.9 3.7-3.9" stroke="#111" stroke-width="1.6" fill="none"/></svg></li>
  </ul>
</section>

<section class="card card--contact">
  <div class="mesh-panel" role="img" aria-label="Dark perforated metal texture"></div>
  <svg class="silver-band" viewBox="0 0 640 366" aria-hidden="true">
    <defs>
      <linearGradient id="contactSilver" x1="0" y1="0" x2="1" y2="0">
        <stop offset="0" stop-color="#ffffff"/>
        <stop offset="0.25" stop-color="#d6d6d6"/>
        <stop offset="0.6" stop-color="#5c5c5c"/>
        <stop offset="1" stop-color="#3a3a3a"/>
      </linearGradient>
    </defs>
    <polygon points="300,205 640,205 640,262 326,262" fill="url(#contactSilver)"/>
  </svg>
  <div class="brand">
    <span class="brand__name">KTR</span>
    <span class="brand__suffix">Pty Ltd</span>
  </div>
  <div class="person">
    <h1 class="person__name">DANIEL HARPER</h1>
    <p class="person__title">Director &amp; Founder</p>
    <div class="person__rule"></div>
    <p class="contact-line">
      <svg viewBox="0 0 16 16" aria-hidden="true"><path d="M4 1.5l2.2 3-1.4 1.6c.8 1.9 2.2 3.3 4.1 4.1l1.6-1.4 3 2.2-1.3 2.5C7 13.2 2.8 9 2.3 3z" fill="none" stroke="#c9c9c9" stroke-width="1.3"/></svg>
      (123) 456-7890
    </p>
    <p class="contact-line contact-line--email">
      <svg viewBox="0 0 16 16" aria-hidden="true"><rect x="1.5" y="3.5" width="13" height="9" fill="#9a9a9a"/><path d="M1.5 3.5l6.5 5 6.5-5" stroke="#0b0b0b" stroke-width="1.2" fill="none"/></svg>
      info@yourwebsite.com
    </p>
  </div>
  <p class="address">Your Address, City<br>State, Zip 1235</p>
</section>

</body>
</html>
```